Online retail store selling a multitude of product categories needs a BigCommerce website

We need a website for our online store. We sell over the counter products such as allergy medicine, antacids, and nutritional supplements on several large market places. We want to have a website that can provide our customers with the ease of navigation and quick access to find the products they are searching for, as well as other products, related to their category. The site should have a modern design that fits our products.

Target Market(s)

Consumer of health, household and beauty products.

Font styles to use
Serif
Sans Serif

Colors

Designer to choose colors to be used in the design.

Requirements
Must have
• • Homepage
• • Shop page - in the shop page there should be our product categories
• • Our Operation
• • Contact Us
Nice to have
• I want the site to be organized and well structured.
Should not have
• Not too busy or overstimulating

```html
<!DOCTYPE html>
<html lang="en">
<head>
<meta charset="utf-8">
<title>Brightway Deal</title>
<link href="https://fonts.googleapis.com/css2?family=Lato:wght@400;700;900&display=swap" rel="stylesheet">
<style>
:root{
  --green:#5aa84f;
  --green-dark:#4b9a43;
  --blue:#1e72b8;
  --teal:#2f8a8f;
  --ink:#222;
  --white:#fff;
  --line:#dfe7df;
}
*{box-sizing:border-box;margin:0;padding:0}
html,body{width:800px;height:1200px;overflow:hidden;background:var(--white);font-family:'Lato',sans-serif;color:var(--ink)}
.page{position:relative;width:800px;height:1200px}
.abs{position:absolute}

/* header */
.search{left:105px;top:43px;width:150px;height:17px;border:2px solid var(--green);border-radius:9px;overflow:hidden;display:flex}
.search span{flex:1;font-size:6.5px;color:#aaa;padding:3px 6px}
.search i{width:27px;background:var(--green);display:flex;align-items:center;justify-content:center}
.brand{left:305px;top:24px;display:flex;align-items:center;gap:7px}
.brand-mark{width:24px;height:24px;background:var(--green)}
.brand-name{font-size:22px;font-weight:900;color:var(--blue);letter-spacing:.5px}
.account{left:610px;top:46px;font-size:7.5px;font-weight:700;color:var(--blue)}
.cart{left:670px;top:38px}

/* nav */
.nav{left:0;top:82px;width:800px;height:37px;background:linear-gradient(90deg,var(--green),var(--teal) 60%,var(--blue))}
.nav a{position:absolute;top:13px;color:var(--white);font-size:9px;font-weight:700;text-decoration:none}
.nav .active{left:254px;top:2px;width:47px;height:35px;background:var(--white);color:var(--green);text-align:center;padding-top:11px}

/* dropdown */
.menu{left:106px;top:119px;width:589px;height:150px;background:var(--white);border:2px solid var(--blue);border-top:none;border-radius:0 0 6px 6px;z-index:5}
.col{position:absolute;top:13px}
.col h3{font-size:8.5px;font-weight:700;color:var(--blue);margin-bottom:6px}
.col li{list-style:none;font-size:5.6px;font-weight:700;color:var(--green);height:19.5px}

/* hero */
.hero{left:105px;top:240px;width:470px;height:210px;border-radius:4px;background:radial-gradient(ellipse at 55% 60%,#8a8a3c,#2f5868 55%,#1f4a60);overflow:hidden}
.hero h1{position:absolute;left:26px;top:29px;color:var(--white);font-size:22px;font-weight:900}
.btn-green{position:absolute;background:var(--green);color:var(--white);border:2px solid var(--white);border-radius:4px;font-weight:900;text-align:center}
.side{left:585px;width:110px;border-radius:4px;overflow:hidden}
.side1{top:240px;height:101px;background:linear-gradient(#c9b6c4,#7aaacf)}
.side2{top:351px;height:99px;background:radial-gradient(circle at 55% 35%,#b8c8c4,#4c7f58 60%,#2f5a35)}
.tag{left:0;top:0;background:var(--green);color:var(--white);font-size:4px;font-weight:700;padding:2px 6px}
.side2 p{position:absolute;top:29px;width:100%;text-align:center;color:var(--white);font-size:7.5px;font-weight:700;line-height:15px}

/* top sellers */
.sellers{left:105px;top:470px;width:590px;height:254px;border:2px solid var(--green);border-radius:8px}
.sellers h2{position:absolute;left:0;top:8px;width:100%;text-align:center;font-size:18px;font-weight:900;color:var(--blue)}
.rule{position:absolute;left:9px;top:35px;width:571px;height:1.5px;background:var(--blue)}
.product{position:absolute;top:53px;width:78px}
.product .img{height:75px;margin:0 auto;border-radius:3px}
.product .name{font-size:7px;line-height:12px;margin-top:6px;height:48px;text-transform:uppercase}
.product .price{font-size:12px;text-align:center;margin-top:5px}
.buy{display:block;width:70px;height:20px;margin:6px auto 0;background:var(--blue);color:var(--white);border-radius:10px;font-size:7px;font-weight:700;text-align:center;line-height:20px}
.arrow{position:absolute;top:118px}

/* story */
.story{left:105px;top:739px;width:590px;height:249px;border-radius:8px;background:linear-gradient(110deg,#8ec285 0%,#5f9a83 40%,#2b6b86 70%,#255a7a 100%);overflow:hidden}
.story h2{position:absolute;top:6px;width:100%;text-align:center;color:var(--white);font-size:17px;font-weight:700}
.story p{position:absolute;left:17px;width:325px;color:var(--white);font-size:7.4px;line-height:16px}

/* footer */
.footer{left:0;top:1003px;width:800px;height:197px;background:linear-gradient(90deg,var(--green),var(--teal) 65%,var(--blue));color:var(--white)}
.footer h2{position:absolute;left:105px;top:26px;font-size:12px;font-weight:400}
.signup{position:absolute;left:470px;top:20px;width:225px;height:23px;background:var(--white);border-radius:12px}
.signup span{position:absolute;left:10px;top:7px;font-size:6.5px;color:#888}
.signup b{position:absolute;right:2px;top:2px;width:52px;height:19px;background:var(--green);border-radius:10px;font-size:7px;text-align:center;line-height:19px;font-weight:700}
.fcol{position:absolute;top:56px}
.fcol h3{font-size:8px;font-weight:700;margin-bottom:8px}
.fcol li{list-style:none;font-size:6.8px;height:18px}
.social{position:absolute;top:95px;width:25px;height:25px;border-radius:50%;background:#dfe8f2}
.copy{position:absolute;top:173px;width:100%;text-align:center;font-size:5.5px}
</style>
</head>
<body>
<div class="page">

  <div class="abs search"><span>SEARCH</span><i><svg width="10" height="10" viewBox="0 0 10 10"><circle cx="4" cy="4" r="3" fill="none" stroke="#fff" stroke-width="1.3"/><line x1="6.2" y1="6.2" x2="9" y2="9" stroke="#fff" stroke-width="1.3"/></svg></i></div>

  <div class="abs brand"><span class="brand-mark"></span><span class="brand-name">BRIGHTWAY DEAL</span></div>

  <div class="abs account">MY ACCOUNT</div>
  <svg class="abs cart" width="26" height="24" viewBox="0 0 26 24">
    <path d="M1 3h4l3 12h13l3-9H6" fill="none" stroke="#1e72b8" stroke-width="1.8"/>
    <line x1="9" y1="9" x2="22" y2="9" stroke="#1e72b8" stroke-width="1.2"/>
    <line x1="10" y1="12" x2="21" y2="12" stroke="#1e72b8" stroke-width="1.2"/>
    <circle cx="10" cy="20" r="2" fill="none" stroke="#1e72b8" stroke-width="1.5"/>
    <circle cx="19" cy="20" r="2" fill="none" stroke="#1e72b8" stroke-width="1.5"/>
    <circle cx="8" cy="5" r="4" fill="#e0261d"/>
    <text x="8" y="7.5" font-size="6" fill="#fff" text-anchor="middle" font-family="Lato,sans-serif">3</text>
  </svg>

  <nav class="abs nav">
    <a style="left:105px">HOME</a>
    <a class="active">SHOP</a>
    <a style="left:429px">OUR OPERATION</a>
    <a style="left:639px">CONTACT US</a>
  </nav>

  <div class="abs hero">
    <div role="img" aria-label="Fish oil softgel capsules spilling from a bottle" style="position:absolute;inset:0"></div>
    <h1>OF FISH OIL</h1>
    <div class="btn-green" style="left:185px;top:110px;width:99px;height:36px;font-size:9px;line-height:32px">SHOP NOW</div>
  </div>

  <div class="abs side side1" role="img" aria-label="Person holding stomach, digestive relief">
    <div class="btn-green" style="left:30px;top:51px;width:54px;height:21px;font-size:6px;line-height:17px">SHOP NOW</div>
  </div>
  <div class="abs side side2" role="img" aria-label="Dandelion seed head in a green field">
    <span class="abs tag">VITAMINS &amp; SUPPLEMENTS</span>
    <p>FIGHT SEASONAL<br>ALLERGIES</p>
    <div class="btn-green" style="left:28px;top:58px;width:54px;height:21px;font-size:6px;line-height:17px">SHOP NOW</div>
  </div>

  <div class="abs menu">
    <ul class="col" style="left:17px"><h3>BEAUTY</h3><li>COSMETICS</li><li>BATH &amp; BODY</li><li>HAIR CARE</li><li>SUN CARE</li><li>FACIAL CARE</li><li>FRAGRANCE</li></ul>
    <ul class="col" style="left:113px"><h3>PERSONAL CARE</h3><li>HAIR CARE</li><li>SUN CARE</li><li>ORAL CARE</li><li>DEODERANT</li><li>SHAVING</li><li>BATH &amp; BODY</li></ul>
    <ul class="col" style="left:245px"><h3>VITAMINS AND SUPPLEMENTS</h3><li>MULTIVITAMINS</li><li>SUPPLEMENTS</li><li>VITAMINS A-K</li><li>HERBS</li><li>FISH OIL AND OMEGAS</li><li>HEALTH</li></ul>
    <ul class="col" style="left:438px"><h3>MEDICINES AND TREATMENTS</h3><li>ALLERGY &amp; SINUS</li><li>COLD &amp; COUGH</li><li>FIRST AID</li><li>DIGESTIVE</li><li>PAIN RELIEF</li><li>CHILDREN'S</li></ul>
  </div>

  <section class="abs sellers">
    <h2>TOP SELLERS</h2>
    <div class="rule"></div>
    <svg class="arrow" style="left:10px" width="10" height="20" viewBox="0 0 10 20"><path d="M9 1L1 10l8 9" fill="none" stroke="#5aa84f" stroke-width="1"/></svg>
    <svg class="arrow" style="left:568px" width="10" height="20" viewBox="0 0 10 20"><path d="M1 1l8 9-8 9" fill="none" stroke="#5aa84f" stroke-width="1"/></svg>

    <div class="product" style="left:52px"><div class="img" role="img" aria-label="Antacid tablet bottle" style="width:36px;background:linear-gradient(#6a2c8f 0 18%,#e9edf2 18%)"></div>
      <div class="name">Calmora Advanced Antacid Tablets Assorted Berries (75 ea)75 EA</div><div class="price">$7.50</div><span class="buy">BUY NOW</span></div>
    <div class="product" style="left:140px"><div class="img" role="img" aria-label="Allergy relief tablets box" style="width:62px;background:linear-gradient(#1f5fae,#f2b53a)"></div>
      <div class="name">Breezon 24HR Allergy Relief Antihistamine Tablets, 80CT</div><div class="price">$28.00</div><span class="buy">BUY NOW</span></div>
    <div class="product" style="left:219px"><div class="img" role="img" aria-label="Men's multivitamin bottle" style="width:38px;background:linear-gradient(#1c3f7a 0 10%,#f2f4f7 10% 40%,#1f4f9e 40% 80%,#f2f4f7 80%)"></div>
      <div class="name">Vitarise Men's Multivitamin, 200 CT.</div><div class="price">$15.00</div><span class="buy">BUY NOW</span></div>
    <div class="product" style="left:299px"><div class="img" role="img" aria-label="Whey protein powder tub" style="width:40px;background:linear-gradient(#222,#b3202a 60%,#222)"></div>
      <div class="name">Forgeline Sport Whey Protein Powder, 2 LB</div><div class="price">$18.00</div><span class="buy">BUY NOW</span></div>
    <div class="product" style="left:377px;width:80px"><div class="img" role="img" aria-label="Argan oil bottle" style="width:32px;background:linear-gradient(#c9a43a,#e8c94a)"></div>
      <div class="name">Lumé Restoring Argan Oil Extra Strength 3.3 Ounce</div><div class="price">$10.00</div><span class="buy">BUY NOW</span></div>
    <div class="product" style="left:459px"><div class="img" role="img" aria-label="Two sunscreen tubes" style="width:40px;background:linear-gradient(#dfe6f0,#9fb2cc 70%,#2a2a2a)"></div>
      <div class="name">Clearwell Light Touch Sunscreen SPF 45, 3 FL. OZ, Pack of 2</div><div class="price">$14.50</div><span class="buy">BUY NOW</span></div>
  </section>

  <section class="abs story" role="img" aria-label="Smiling woman outdoors by the sea">
    <h2>LIVE YOUR BEST LIFE WITH BRIGHTWAY DEAL</h2>
    <p style="top:41px">Lorem ipsum dolor sit amet, consectetur adipiscing elit, sed do eiusmod tempor incididunt ut labore et dolore magna aliqua. Praesent elementum facilisis leo vel fringilla est ullamcorper. Arcu vitae elementum curabitur vitae nunc sed velit dignissim sodales. Vehicula ipsum a arcu cursus. Pulvinar proin gravida hendrerit lectus. Purus gravida quis blandit turpis.</p>
    <p style="top:121px">Cursus in hac habitasse platea. Et malesuada fames ac turpis egestas sed tempus. Tincidunt praesent semper feugiat nibh sed pulvinar proin. Quam vulputate dignissim suspendisse in. Pellentesque eu tincidunt tortor aliquam nulla. Quis imperdiet massa tincidunt nunc pulvinar sapien et ligula ullamcorper. Varius duis at consectetur lorem donec.</p>
  </section>

  <footer class="abs footer">
    <h2>SIGN UP FOR OUR NEWSLETTER AND GET EXCLUSIVE DEALS</h2>
    <div class="signup"><span>GET EMAILS FROM US</span><b>SIGN UP</b></div>
    <ul class="fcol" style="left:105px"><h3>COMPANY INFO</h3><li>About Us</li><li>Contact Us</li></ul>
    <ul class="fcol" style="left:254px"><h3>MY ACCOUNT</h3><li>My Account</li><li>Create Account</li><li>Shopping Cart</li></ul>
    <span class="social" style="left:580px" aria-label="Social link"></span>
    <span class="social" style="left:610px" aria-label="Social link"></span>
    <span class="social" style="left:640px" aria-label="Social link"></span>
    <span class="social" style="left:670px" aria-label="Social link"></span>
    <div class="copy">COPYRIGHT 2019 BRIGHTWAYDEAL.</div>
  </footer>

</div>
</body>
</html>
```